Alpforma Banner

Hi boys and girls :)

We have a little project 4u.

We need a banner in 4 sizes :

Leaderboard: 728*90
Wide SkyScraper: 160*600
Medium Rectangle: 300*250
Ribbon (special format): 990*45

Message on banner :

Either our Logo + Immigration, Integration, Naturalization

Or our Logo + Incorporation, Domicile, Secretarial Services

And if space allows for it www.alpforma-example.com as well.

We are looking for a clean design, check our Website for inspiration concerning colors.

```html
<!DOCTYPE html>
<html lang="en">
<head>
<meta charset="utf-8">
<title>Alpforma Banner Set</title>
<link rel="stylesheet" href="https://fonts.googleapis.com/css2?family=Josefin+Sans:wght@300;400&display=swap">
<style>
  :root {
    --stage: #3a2f2a;
    --silver-light: #f4f4f4;
    --silver-mid: #c9c9c9;
    --silver-dark: #8f8f8f;
    --ink: #1d1d1d;
    --paper: #ffffff;
    --pill-grey: #9a9ca3;
    --pill-dark: #3b3b3b;
    --sky-light: #e6e6e6;
    --sky-dark: #9c9c9c;
  }
  * { box-sizing: border-box; margin: 0; padding: 0; }
  html, body { width: 1200px; height: 1000px; overflow: hidden; }
  body {
    background: var(--stage);
    font-family: "Josefin Sans", sans-serif;
    font-weight: 300;
    color: var(--ink);
    position: relative;
  }
  .banner {
    position: absolute;
    overflow: hidden;
    background: radial-gradient(ellipse at 45% 55%, var(--silver-light) 0%, var(--silver-mid) 60%, var(--silver-dark) 100%);
    box-shadow: 0 2px 6px rgba(0,0,0,0.45);
  }
  .photo {
    position: absolute;
    background: linear-gradient(160deg, var(--sky-light) 0%, var(--sky-dark) 100%);
    opacity: 0.75;
  }
  .brand {
    position: absolute;
    color: var(--paper);
    font-weight: 400;
    letter-spacing: 1px;
    text-shadow: none;
    text-align: center;
  }
  .services { position: absolute; text-align: center; letter-spacing: 1px; }
  .services span { display: block; }
  .url { position: absolute; color: var(--paper); letter-spacing: 1px; font-weight: 400; }

  /* skyscrapers */
  .sky-a { left: 52px; top: 205px; width: 158px; height: 598px; }
  .sky-b { left: 241px; top: 205px; width: 160px; height: 598px; }
  .sky-a .photo { left: 20px; top: 0; width: 138px; height: 330px; }
  .sky-b .photo { left: 40px; top: 255px; width: 120px; height: 343px; }
  .sky-a .services { left: 0; right: 0; top: 224px; font-size: 21px; }
  .sky-a .services span { margin-bottom: 34px; }
  .sky-b .services { left: 0; right: 0; top: 52px; font-size: 21px; color: var(--paper); }
  .sky-b .services span { margin-bottom: 33px; }
  .sky .brand { left: 0; right: 0; bottom: 34px; font-size: 26px; }
  .sky .url { left: 0; right: 0; bottom: 6px; text-align: center; font-size: 14px; }

  /* rectangles */
  .rect-a { left: 434px; top: 205px; width: 300px; height: 248px; }
  .rect-b { left: 765px; top: 205px; width: 300px; height: 248px; }
  .rect-a .photo { left: 170px; top: 0; width: 130px; height: 248px; }
  .rect-b .photo { left: 185px; top: 0; width: 90px; height: 248px; }
  .rect .brand { left: 30px; width: 150px; top: 30px; font-size: 30px; }
  .rect-a .services { left: 20px; width: 170px; top: 106px; font-size: 21px; }
  .rect-b .services { left: 10px; width: 175px; top: 101px; font-size: 23px; }
  .rect .services span { margin-bottom: 11px; }
  .rect-a .url { left: 8px; bottom: 4px; font-size: 14px; }
  .rect-b .url { left: 8px; bottom: 4px; font-size: 16px; }

  /* leaderboards */
  .leader { left: 434px; width: 728px; height: 88px; }
  .lead-a { top: 487px; }
  .lead-b { top: 604px; }
  .lead-c { top: 718px; }
  .leader .brand { left: 12px; width: 120px; top: 28px; font-size: 26px; }
  .leader .services {
    left: 142px; right: 0; top: 22px; height: 40px;
    display: flex; align-items: center; justify-content: space-between;
    padding: 0 12px 0 22px; font-size: 24px;
  }
  .lead-a .services { background: var(--pill-grey); color: var(--paper); border-radius: 10px 0 0 10px; }
  .lead-c .services { background: var(--pill-dark); color: var(--paper); border-radius: 10px 0 0 10px; }
  .lead-b .services { left: 140px; padding: 0 26px 0 10px; }
  .leader .url { right: 6px; bottom: 5px; font-size: 12px; }
</style>
</head>
<body>

  <section class="banner sky sky-a">
    <div class="photo" role="img" aria-label="Black and white photo of a waving flag on a pole"></div>
    <div class="services"><span>Immigration</span><span>Integration</span><span>Naturalization</span></div>
    <div class="brand">Alpforma</div>
    <div class="url">alpforma-example.com</div>
  </section>

  <section class="banner sky sky-b">
    <div class="photo" role="img" aria-label="Black and white photo of a flag on a tall pole against the sky"></div>
    <div class="services"><span>Immigration</span><span>Integration</span><span>Naturalization</span></div>
    <div class="brand">Alpforma</div>
    <div class="url">alpforma-example.com</div>
  </section>

  <section class="banner rect rect-a">
    <div class="photo" role="img" aria-label="Black and white photo of a waving flag on a pole"></div>
    <div class="brand">Alpforma</div>
    <div class="services"><span>Immigration</span><span>Integration</span><span>Naturalization</span></div>
    <div class="url">www.alpforma-example.com</div>
  </section>

  <section class="banner rect rect-b">
    <div class="photo" role="img" aria-label="Black and white photo of a flag on a tall pole"></div>
    <div class="brand">Alpforma</div>
    <div class="services"><span>Immigration</span><span>Integration</span><span>Naturalization</span></div>
    <div class="url">www.alpforma-example.com</div>
  </section>

  <section class="banner leader lead-a">
    <div class="brand">Alpforma</div>
    <div class="services"><span>Immigration</span><span>Integration</span><span>Naturalization</span></div>
    <div class="url">www.alpforma-example.com</div>
  </section>

  <section class="banner leader lead-b">
    <div class="brand">Alpforma</div>
    <div class="services"><span>Immigration</span><span>Integration</span><span>Naturalization</span></div>
    <div class="url">www.alpforma-example.com</div>
  </section>

  <section class="banner leader lead-c">
    <div class="brand">Alpforma</div>
    <div class="services"><span>Immigration</span><span>Integration</span><span>Naturalization</span></div>
    <div class="url">www.alpforma-example.com</div>
  </section>

</body>
</html>
```